Corporate Design für Institut im Bereich der Führungskräfteausbildung
Zielgruppe
Führungskräfteausbildung, Unternehmensberatung,
www.brelox.at
Aufgabenstellung
Bekanntes Unternehmen, sehr erfolgreich

```html
<!DOCTYPE html>
<html lang="de">
<head>
<meta charset="utf-8">
<title>Brelox Akademie – Geschäftsausstattung</title>
<link href="https://fonts.googleapis.com/css2?family=Open+Sans:wght@400;600;700&display=swap" rel="stylesheet">
<style>
  :root {
    --navy: #0f4477;
    --navy-deep: #0c3a66;
    --paper: #ffffff;
    --ink: #2b2b2b;
    --ink-soft: #555a60;
    --backdrop: #e4e7e8;
    --window: #d6d6d6;
    --rule: #9aa0a6;
  }
  * { box-sizing: border-box; margin: 0; padding: 0; }
  html, body { width: 1200px; height: 900px; overflow: hidden; }
  body {
    background: var(--backdrop);
    font-family: "Open Sans", sans-serif;
    color: var(--ink);
    position: relative;
  }
  .sheet { position: absolute; background: var(--paper); box-shadow: 0 2px 6px rgba(0,0,0,.12); }

  /* wordmark */
  .wordmark { display: flex; align-items: center; gap: 8px; color: var(--navy); font-weight: 600; letter-spacing: .08em; text-transform: uppercase; line-height: 1.15; }
  .wordmark .mark { background: var(--navy); border-radius: 4px; flex: none; }
  .wordmark.on-dark { color: var(--paper); }
  .wordmark.on-dark .mark { background: var(--paper); }

  /* business cards */
  .card { width: 255px; height: 160px; overflow: hidden; }
  .card-back { left: 40px; top: 60px; background: var(--navy); display: flex; align-items: center; justify-content: center; }
  .card-back .wordmark { font-size: 12px; }
  .card-back .mark { width: 22px; height: 22px; }
  .card-front { left: 40px; top: 250px; }
  .card-front .wordmark { position: absolute; left: 16px; top: 44px; font-size: 9px; }
  .card-front .mark { width: 16px; height: 16px; }
  .card-front .divider { position: absolute; left: 128px; top: 22px; width: 1px; height: 96px; background: var(--rule); }
  .card-front .person { position: absolute; left: 142px; top: 24px; font-size: 8px; color: var(--navy); }
  .card-front .person strong { display: block; font-size: 9px; font-weight: 700; }
  .contact-list { list-style: none; position: absolute; left: 142px; top: 56px; font-size: 7.5px; color: var(--ink-soft); }
  .contact-list li { display: flex; align-items: center; gap: 6px; height: 15px; }
  .contact-list svg { width: 10px; height: 10px; flex: none; }
  .band { position: absolute; left: 0; right: 0; bottom: 0; background: var(--navy); }
  .card-front .band { height: 10px; }

  /* invoice */
  .invoice { left: 335px; top: 40px; width: 400px; height: 566px; font-size: 8px; }
  .invoice .sender { position: absolute; left: 40px; top: 48px; font-size: 6.5px; line-height: 1.35; color: var(--ink-soft); }
  .invoice .wordmark { position: absolute; right: 40px; top: 42px; font-size: 9px; }
  .invoice .mark { width: 20px; height: 20px; }
  .invoice .recipient { position: absolute; left: 40px; top: 92px; font-size: 9px; color: var(--ink-soft); }
  .invoice h1 { position: absolute; left: 40px; top: 150px; font-size: 22px; font-weight: 600; }
  .invoice .meta { position: absolute; left: 40px; top: 184px; display: grid; grid-template-columns: 90px auto; row-gap: 2px; font-size: 8px; }
  .lines { position: absolute; left: 40px; top: 240px; width: 320px; border-collapse: collapse; font-size: 8px; }
  .lines th { text-align: left; font-weight: 700; padding-bottom: 4px; }
  .lines td { padding: 2px 0; color: var(--ink-soft); }
  .totals { position: absolute; left: 190px; top: 330px; width: 170px; font-size: 8.5px; }
  .totals div { display: flex; justify-content: space-between; padding: 3px 0; }
  .totals .grand { border-top: 1px solid var(--ink); font-weight: 700; margin-top: 2px; }
  .invoice .footer { position: absolute; left: 40px; right: 40px; bottom: 34px; display: flex; justify-content: space-between; font-size: 6px; line-height: 1.4; color: var(--ink-soft); }
  .invoice .band { height: 14px; }

  /* envelope */
  .envelope { left: 40px; top: 640px; width: 500px; height: 230px; }
  .envelope .wordmark { position: absolute; left: 30px; top: 32px; font-size: 14px; }
  .envelope .mark { width: 34px; height: 34px; }
  .envelope .window { position: absolute; right: 30px; top: 82px; width: 200px; height: 90px; background: var(--window); border-radius: 8px; }
  .envelope .band { height: 14px; }

  /* folder */
  .folder { left: 780px; top: 250px; width: 380px; height: 537px; background: linear-gradient(160deg, var(--navy) 0%, var(--navy-deep) 100%); display: flex; align-items: center; justify-content: center; }
  .folder .wordmark { font-size: 18px; gap: 14px; }
  .folder .mark { width: 40px; height: 40px; border-radius: 6px; }
</style>
</head>
<body>

  <section class="sheet card card-back" aria-label="Visitenkarte Rückseite">
    <div class="wordmark on-dark"><span class="mark"></span><span>Brelox Akademie</span></div>
  </section>

  <section class="sheet card card-front" aria-label="Visitenkarte Vorderseite">
    <div class="wordmark"><span class="mark"></span><span>Brelox<br>Akademie</span></div>
    <div class="divider"></div>
    <p class="person"><strong>Name Surname</strong>Director</p>
    <ul class="contact-list">
      <li><svg viewBox="0 0 10 10"><path d="M5 1a3 3 0 0 1 3 3c0 2-3 5-3 5S2 6 2 4a3 3 0 0 1 3-3z" fill="none" stroke="#0f4477"/><circle cx="5" cy="4" r="1" fill="#0f4477"/></svg>Street + nr</li>
      <li><svg viewBox="0 0 10 10"><rect x="3" y="1" width="4.5" height="8" rx="1" fill="none" stroke="#0f4477"/></svg>06 12345678</li>
      <li><svg viewBox="0 0 10 10"><circle cx="5" cy="5" r="4" fill="none" stroke="#0f4477"/><path d="M1 5h8M5 1c2 2 2 6 0 8M5 1c-2 2-2 6 0 8" fill="none" stroke="#0f4477" stroke-width=".7"/></svg>www.brelox.at</li>
      <li><svg viewBox="0 0 10 10"><rect x="1" y="2.5" width="8" height="5.5" fill="none" stroke="#0f4477"/><path d="M1 2.5l4 3 4-3" fill="none" stroke="#0f4477"/></svg>info@emailadres.nl</li>
    </ul>
    <div class="band"></div>
  </section>

  <section class="sheet invoice" aria-label="Rechnung">
    <p class="sender">Brelox<br>Adress<br>City</p>
    <div class="wordmark"><span class="mark"></span><span>Brelox<br>Akademie</span></div>
    <p class="recipient">Recipient address</p>
    <h1>Invoice</h1>
    <div class="meta">
      <span>Date:</span><span>09-05-2018</span>
      <span>Invoicenumer:</span><span>1042018</span>
      <span>Relatienummer:</span><span>31</span>
    </div>
    <table class="lines">
      <thead><tr><th>QTY</th><th>Description</th><th>Price</th><th>Total</th><th>BTW</th></tr></thead>
      <tbody><tr><td>1</td><td>Logo variations</td><td>€ 150,-</td><td>€ 150,-</td><td>0%</td></tr></tbody>
    </table>
    <div class="totals">
      <div><span>Total excl. BTW:</span><span>€ 150,-</span></div>
      <div><span>BTW Verlegd</span><span>€ 0,-</span></div>
      <div class="grand"><span>Total incl. BTW:</span><span>€ 150,-</span></div>
    </div>
    <div class="footer">
      <span>www.brelox.at</span>
      <span>Straat plus huisnr.<br>info@email.nl</span>
      <span>1234 AA UTRECHT<br>KVK: 12345678</span>
      <span>T. 06-123456789<br>BANK: NL 00 RBRB 0123 4567 89</span>
    </div>
    <div class="band"></div>
  </section>

  <section class="sheet envelope" aria-label="Briefumschlag">
    <div class="wordmark"><span class="mark"></span><span>Brelox<br>Akademie</span></div>
    <div class="window"></div>
    <div class="band"></div>
  </section>

  <section class="sheet folder" aria-label="Mappe">
    <div class="wordmark on-dark"><span class="mark"></span><span>Brelox<br>Akademie</span></div>
  </section>

</body>
</html>
```